Tarvell homes and renovations business card design.

Would like some new card designs utilizing my new logo that look professional. I am open to different colors on the logo or utilize the same ones we have. I like the original concept but would like to see some fresh ideas and build on what we have already done.

Target Market(s)

Custom home building industry, Real estate sales, Renovation projects.

Industry/Entity Type

Home Builder

Contact Information for Business Card

Tarvell Homes and Renovations
2871 162nd Street
Brackwell, Northcrest
T0L3P0
Home : 403- 555-0187 Cell: 403- 555-0243

My info is : Gus Tarvell, President and CEO
email: tarvellhomes@quillmail.example
Website: tarvellhomes.example

Requirements
Must have
• Must Use my new logo design. I am open to different colors on the logo or utilize the same ones in the existing design. I can upload the original logo design if needed.

```html
<!DOCTYPE html>
<html lang="en">
<head>
<meta charset="utf-8">
<title>Tarvell Homes and Renovations – Business Card</title>
<link rel="stylesheet" href="https://fonts.googleapis.com/css2?family=Montserrat:wght@600&family=Arimo:wght@400;700&display=swap">
<style>
  :root {
    --backdrop: #2a2a2a;
    --card-white: #fbfbfb;
    --card-black: #0b0b0b;
    --gold: #e2aa1c;
    --bronze: #a87a2a;
    --grey-text: #d6d6d6;
  }
  * { box-sizing: border-box; margin: 0; padding: 0; }
  html, body {
    width: 1200px; height: 997px; overflow: hidden;
    background: var(--backdrop);
  }
  .stage { position: relative; width: 1200px; height: 997px; }
  .card {
    position: absolute; left: 250px; width: 700px; height: 400px;
    background: var(--card-white);
    overflow: hidden;
    box-shadow: 0 12px 30px rgba(0,0,0,.5);
  }
  .card--back { top: 60px; }
  .card--front { top: 537px; }

  .band {
    position: absolute; left: 0; right: 0; bottom: 0;
    background: var(--card-black);
  }
  .band__rule {
    position: absolute; left: 0; right: 0; height: 3px; background: var(--gold);
  }
  .band__rule--one { top: 10px; }
  .band__rule--two { top: 20px; }
  .card--front .band { top: 262px; }
  .card--back .band { top: 205px; }

  .brand {
    position: absolute;
    display: flex; align-items: center; gap: 12px;
    font-family: "Montserrat", sans-serif; font-weight: 600;
    color: var(--bronze);
    white-space: nowrap;
  }
  .brand__mark { width: 14px; height: 14px; background: var(--bronze); }
  .card--front .brand { left: 0; right: 0; top: 110px; justify-content: center; font-size: 34px; }
  .card--back .brand { left: 40px; top: 88px; font-size: 24px; }

  .website {
    position: absolute; left: 0; right: 0; bottom: 40px; text-align: center;
    font-family: "Arimo", sans-serif; font-size: 20px; letter-spacing: 2px;
    color: var(--gold);
  }

  .holder {
    position: absolute; left: 40px; top: 80px;
    font-family: "Arimo", sans-serif;
  }
  .holder__name { color: var(--gold); font-weight: 700; font-size: 19px; text-transform: uppercase; }
  .holder__title { color: var(--grey-text); font-size: 16px; margin-top: 6px; text-transform: uppercase; }

  .divider {
    position: absolute; left: 330px; top: 50px; width: 2px; height: 100px; background: var(--gold);
  }

  .contacts {
    position: absolute; left: 360px; top: 42px; list-style: none;
    font-family: "Arimo", sans-serif; font-size: 14px; color: var(--grey-text);
  }
  .contacts li { display: flex; align-items: flex-start; gap: 10px; line-height: 18px; margin-bottom: 6px; }
  .contacts svg { flex: none; width: 16px; height: 16px; margin-top: 1px; }
</style>
</head>
<body>
<main class="stage">

  <section class="card card--back" aria-label="Business card, back">
    <div class="brand"><span class="brand__mark"></span>Tarvell Homes and Renovations</div>
    <div class="band">
      <div class="band__rule band__rule--one"></div>
      <div class="band__rule band__rule--two"></div>
      <div class="holder">
        <p class="holder__name">Gus Tarvell</p>
        <p class="holder__title">President and CEO</p>
      </div>
      <div class="divider"></div>
      <ul class="contacts">
        <li>
          <svg viewBox="0 0 16 16" aria-hidden="true"><rect width="16" height="16" rx="3" fill="var(--gold)"/><path d="M4 5c0-1 1-1.5 1.5-1.5L7 5.5 6 7c.6 1.3 1.6 2.3 3 3l1.5-1 2 1.5c0 .5-.5 1.5-1.5 1.5C7.5 12 4 8.5 4 5z" fill="#000"/></svg>
          <span>403- 555-0187</span>
        </li>
        <li>
          <svg viewBox="0 0 16 16" aria-hidden="true"><rect width="16" height="16" rx="3" fill="var(--gold)"/><rect x="5.5" y="3" width="5" height="10" rx="1" fill="#000"/><rect x="6.5" y="4.5" width="3" height="6" fill="var(--gold)"/></svg>
          <span>403- 555-0243</span>
        </li>
        <li>
          <svg viewBox="0 0 16 16" aria-hidden="true"><rect width="16" height="16" rx="3" fill="var(--gold)"/><rect x="3" y="5" width="10" height="7" fill="#000"/><path d="M3 5l5 4 5-4" stroke="var(--gold)" stroke-width="1" fill="none"/></svg>
          <span>tarvellhomes@quillmail.example</span>
        </li>
        <li>
          <svg viewBox="0 0 16 16" aria-hidden="true"><rect width="16" height="16" rx="3" fill="var(--gold)"/><path d="M8 3a3.5 3.5 0 0 0-3.5 3.5C4.5 9 8 13 8 13s3.5-4 3.5-6.5A3.5 3.5 0 0 0 8 3z" fill="#000"/><circle cx="8" cy="6.5" r="1.3" fill="var(--gold)"/></svg>
          <span>2871 162nd Street Brackwell, Northcrest<br>T0L3P0</span>
        </li>
      </ul>
    </div>
  </section>

  <section class="card card--front" aria-label="Business card, front">
    <div class="brand"><span class="brand__mark"></span>Tarvell Homes and Renovations</div>
    <div class="band">
      <div class="band__rule band__rule--one"></div>
      <div class="band__rule band__rule--two"></div>
      <p class="website">www.tarvellhomes.example</p>
    </div>
  </section>

</main>
</body>
</html>
```